Website Design for a High School

School Name: Bayt Nakhla Private Schools
sub-schools:
1-Bayt Nakhla Primary School
2-Bayt Nakhla High School for Girls
3-Bayt Nakhla High School for Boys
The design should be professional and serious and below is the details of the website.
Pages: (Home, About Us, Schools, Events, Students, Gallery, Lectures, Contact Us).
A-) Home Page:
1-Animated photos banner as main
2-Marquee for the last news.
3-Welcoming block of text
4-latest news at the body of the page.
5-Calender "on the side"
6-Number of visitors "on the side"
7-Search bar
8-options to choose a school
B-) School Page:
three schools listed as drop down menu when highlighted over the Schools button in the menu
*Each school page should contain:
1-Student login area
2-Animation photos header
3-Specific news and projects
C-) Student Login page:
have a Report Card
D-) Gallery Page
have a collection of photos.
E-)Contact Page
phone numbers
emails
feedback form
F-)Other mentioned pages
with normal text and photos page look as similar to the Home page.
Required color: Purple as main and include the logo colors
Logo: is attached.
Button link to change language to Arabic.
School
5+ page

```html
<!DOCTYPE html>
<html lang="en">
<head>
<meta charset="utf-8">
<title>Bayt Nakhla Private Schools</title>
<link rel="stylesheet" href="https://fonts.googleapis.com/css2?family=Raleway:wght@400;500;600&family=Open+Sans:wght@400;600;700&family=Roboto+Slab:wght@400;500&display=swap">
<style>
:root{
  --purple:#5a2d91;
  --purple-dark:#3f1b73;
  --purple-light:#8a5cc0;
  --gold:#f7c24e;
  --gold-light:#fde69a;
  --ink:#2c2c2c;
  --muted:#777;
  --line:#d9d9d9;
  --white:#fff;
}
*{margin:0;padding:0;box-sizing:border-box}
html,body{width:967px;height:1200px;overflow:hidden;background:var(--white);font-family:"Open Sans",sans-serif;color:var(--ink)}
.page{position:relative;width:967px;height:1200px}
.abs{position:absolute}

.lang{left:778px;top:27px;width:71px;height:20px;border:1px solid #ccc;font-size:9px;display:flex;align-items:center;gap:5px;padding-left:7px;color:#333;background:#fff}
.lang .flag{width:14px;height:9px;background:#1f3f8f;border:1px solid #c22}
.lang .caret{width:0;height:0;border-left:3px solid transparent;border-right:3px solid transparent;border-top:4px solid #555}
.search{left:675px;top:56px;width:175px;height:22px;border:1px solid #bbb;font-size:8px;font-style:italic;color:#666;display:flex;align-items:center;justify-content:space-between;padding:0 7px 0 9px;background:#fafafa}

.nav{left:0;top:87px;width:967px;height:41px;background:linear-gradient(var(--purple-light),var(--purple))}
.nav a{position:absolute;top:0;height:41px;line-height:41px;color:var(--white);font-size:11.5px;text-decoration:none;font-family:"Open Sans",sans-serif}
.nav .sep{position:absolute;top:0;width:1px;height:41px;background:rgba(255,255,255,.25)}

.brand{left:415px;top:20px;width:134px;height:134px;border-radius:50%;background:var(--white);border:4px solid var(--purple-dark);display:flex;flex-direction:column;align-items:center;justify-content:center;text-align:center;padding:16px}
.brand .dot{width:16px;height:16px;border-radius:50%;background:var(--gold);margin-bottom:6px}
.brand span{font-family:"Raleway",sans-serif;font-weight:600;font-size:12px;line-height:14px;color:var(--purple-dark)}

.hero{left:0;top:128px;width:967px;height:382px;background:linear-gradient(135deg,#6d7a55 0%,#3a3a35 35%,#1c1c22 60%,#5b6144 100%)}
.hero-caption{left:116px;top:246px;width:394px;height:104px;background:rgba(247,194,78,.88);padding:17px 0 0 28px;font-family:"Roboto Slab",serif;font-size:26px;line-height:34px}
.hero-caption .l1{color:#1b1b1b}
.hero-caption .l2{color:var(--white)}
.dots{left:453px;top:481px;display:flex;gap:4px}
.dots i{width:12px;height:12px;border-radius:50%;background:#eee;display:block}
.dots i.on{background:#c9b81f}

.ticker{left:0;top:510px;width:967px;height:54px;background:linear-gradient(var(--purple-light),var(--purple));color:var(--white);display:flex;align-items:center}
.ticker h3{font-family:"Raleway",sans-serif;font-weight:400;font-size:18px;margin-left:118px;padding-right:14px;border-right:1px solid rgba(255,255,255,.4);line-height:26px}
.ticker p{font-size:12px;margin-left:18px;color:#eadff7}

.welcome{left:117px;top:615px;width:480px}
.welcome h1{font-family:"Raleway",sans-serif;font-weight:400;font-size:24px;color:#333;margin-bottom:8px}
.welcome p{font-size:7.8px;line-height:14px;color:#444;margin-bottom:9px;padding-left:2px}

.visitors{left:657px;top:612px;width:192px;height:93px;background:linear-gradient(var(--purple),var(--purple-dark));color:var(--white);text-align:center;font-family:"Raleway",sans-serif}
.visitors .t{font-size:16px;padding-top:18px}
.visitors .n{font-size:25px;margin-top:4px}
.choose{left:657px;top:713px;width:192px;height:42px;background:linear-gradient(var(--gold-light),var(--gold));display:flex;align-items:center;padding-left:14px;gap:8px;font-family:"Raleway",sans-serif;font-size:15.5px;font-weight:500;color:var(--purple-dark)}
.tab{left:853px;top:696px;width:20px;height:29px;background:linear-gradient(var(--purple) 0 33%,var(--gold-light) 33% 66%,var(--purple) 66%)}

.divider{left:117px;top:802px;width:732px;height:3px;border-top:1px solid var(--line);border-bottom:1px solid var(--line)}
.divider-mark{left:476px;top:798px;width:14px;height:9px;background:#fff;border:1px solid #bbb}

.news-title{left:116px;top:843px;font-family:"Raleway",sans-serif;font-size:21px;color:var(--purple)}
.news-item{width:250px}
.news-item h4{font-weight:400;font-size:12.5px;color:#333;margin-bottom:3px}
.news-item p{font-size:7.6px;line-height:14px;color:#888}
.news-item .date{font-size:8px;font-weight:700;color:var(--purple-dark);margin-top:1px}

.cal-title{left:654px;top:841px;font-family:"Raleway",sans-serif;font-size:20px;color:var(--purple)}
.calendar{left:656px;top:875px;width:190px;border-collapse:collapse;font-size:10.5px;text-align:center}
.calendar .head td{background:var(--purple-dark);color:#fff;height:26px;font-size:10.5px}
.calendar .days td{background:linear-gradient(var(--gold-light),var(--gold));height:20px;font-size:9.5px;color:#333}
.calendar .wk td{border:1px solid var(--line);height:21.4px;width:27px;color:#222}
.calendar .wk td.off{color:#aaa}
.calendar .wk td.today{background:var(--purple-dark);color:#fff}

.footer{left:0;top:1103px;width:967px;height:97px;background:linear-gradient(var(--gold-light),var(--gold))}
.footer-links{left:115px;top:1130px;font-family:"Raleway",sans-serif;font-weight:600;font-size:12px;color:var(--purple-dark);word-spacing:1px}
.copyright{left:115px;top:1153px;font-size:9px;color:#333}
.social{left:780px;top:1127px;display:flex;gap:5px}
.social i{display:block;width:19px;height:19px;border-radius:3px;background:var(--purple-dark)}
</style>
</head>
<body>
<div class="page">

  <div class="abs lang"><span class="flag"></span>English<span class="caret"></span></div>
  <div class="abs search">Search here
    <svg width="12" height="12" viewBox="0 0 12 12"><circle cx="5" cy="5" r="3.8" fill="none" stroke="#888" stroke-width="1.4"/><line x1="8" y1="8" x2="11" y2="11" stroke="#888" stroke-width="1.6"/></svg>
  </div>

  <nav class="abs nav">
    <a style="left:152px">HOME</a><span class="sep" style="left:192px"></span>
    <a style="left:201px">ABOUT US</a><span class="sep" style="left:264px"></span>
    <a style="left:273px">SCHOOLS</a><span class="sep" style="left:333px"></span>
    <a style="left:342px">EVENTS</a>
    <a style="left:568px">STUDENTS</a><span class="sep" style="left:633px"></span>
    <a style="left:642px">GALLERY</a><span class="sep" style="left:699px"></span>
    <a style="left:708px">LECTURES</a><span class="sep" style="left:771px"></span>
    <a style="left:780px">CONTACT US</a>
  </nav>

  <div class="abs brand"><i class="dot"></i><span>Bayt Nakhla Private Schools</span></div>

  <div class="abs hero" role="img" aria-label="Group of smiling graduates in caps and gowns holding diplomas outdoors"></div>
  <div class="abs hero-caption"><div class="l1">PROIN DUI LECTUS</div><div class="l2">PERIMARY &amp; HIGH SCHOOL</div></div>
  <div class="abs dots"><i class="on"></i><i></i><i></i><i></i></div>

  <div class="abs ticker"><h3>LAST NEWS</h3><p>Vivamus porttitor purus nisi eleifend libero a tempus libero lectus feugiat felis Morbi diam mauris</p></div>

  <section class="abs welcome">
    <h1>Welcome to Our Website Mainpage</h1>
    <p>Vivamus porttitor purus nisi eleifend libero a tempus libero lectus feugiat felis Morbi diam mauris viverra in gravida eu mattis in ante Morbi eget arcu Morbi porta libero id ullamcorper nonummy nibh ligula pulvinar metus eget consectetuer augue nisi quis lacus Ut ac mi quis lacus mollis aliquam Curabitur iaculis tempus eros</p>
    <p>Curabitur vel mi sit amet magna malesuada ultrices Ut nisi erat fermentum vel congue id euismod in elit Fusce ultricies orci ac feugiat suscipit leo massa sodales velit et scelerisque mi tortor at ipsum cligula augue bibendum accumsan vestibulum ut commodo a mi Morbi ornare gravida elit Integer congue augue et malesuada iaculis ipsum dui aliquet felis at cursus magna nisl nec elit Praesent elementum elit at tellus nec ultricies sit amet porttitor mattis enim In massa libero</p>
  </section>

  <div class="abs visitors"><div class="t">Number of Visitor</div><div class="n">2505</div></div>
  <div class="abs choose">
    <svg width="28" height="22" viewBox="0 0 28 22"><path d="M14 1 L14 6 M14 1 L19 2.5 L14 4" stroke="#3f1b73" stroke-width="1.4" fill="#3f1b73"/><path d="M3 10 L14 5 L25 10 L25 22 L3 22 Z" fill="#3f1b73"/><rect x="12" y="15" width="4" height="7" fill="#fde69a"/><rect x="6" y="13" width="3" height="3" fill="#fde69a"/><rect x="19" y="13" width="3" height="3" fill="#fde69a"/></svg>
    Choose a School
    <svg width="8" height="12" viewBox="0 0 8 12"><path d="M1 1 L6 6 L1 11" stroke="#3f1b73" stroke-width="1.6" fill="none"/></svg>
  </div>
  <div class="abs tab"></div>

  <div class="abs divider"></div>
  <div class="abs divider-mark"></div>

  <h2 class="abs news-title">Latest News</h2>
  <article class="abs news-item" style="left:118px;top:886px"><h4>Class aptent taciti sociosqu</h4><p>Suspendisse quam leo molestie sed luctus quis feugiat in pede<br>Fusce tellus Sed metus augue conval</p><div class="date">22 April 2015</div></article>
  <article class="abs news-item" style="left:391px;top:886px"><h4>Nunc porta convallis pede</h4><p>Suspendisse quam leo molestie sed luctus quis feugiat in pede<br>Fusce tellus Sed metus augue conval</p><div class="date">22 April 2015</div></article>
  <article class="abs news-item" style="left:117px;top:974px"><h4>Maecenas at justo id velit placerat</h4><p>Suspendisse quam leo molestie sed luctus quis feugiat in pede<br>Fusce tellus Sed metus augue conval</p><div class="date">22 April 2015</div></article>
  <article class="abs news-item" style="left:390px;top:974px"><h4>Fusce ultricies orci ac feugiat</h4><p>Suspendisse quam leo molestie sed luctus quis feugiat in pede<br>Fusce tellus Sed metus augue conval</p><div class="date">22 April 2015</div></article>

  <h2 class="abs cal-title">Our Calender</h2>
  <table class="abs calendar">
    <tr class="head"><td>&#9664;</td><td colspan="5">MAY 2015</td><td>&#9654;</td></tr>
    <tr class="days"><td>Su</td><td>Mo</td><td>Tu</td><td>We</td><td>Th</td><td>Fr</td><td>Sa</td></tr>
    <tr class="wk"><td class="off">28</td><td class="off">29</td><td class="off">30</td><td class="off">31</td><td>1</td><td>2</td><td>3</td></tr>
    <tr class="wk"><td>4</td><td>5</td><td>6</td><td>7</td><td>8</td><td>9</td><td>10</td></tr>
    <tr class="wk"><td>11</td><td>12</td><td>13</td><td>14</td><td>15</td><td>16</td><td>17</td></tr>
    <tr class="wk"><td>18</td><td>19</td><td class="today">20</td><td>21</td><td>22</td><td>23</td><td>24</td></tr>
    <tr class="wk"><td>25</td><td>26</td><td>27</td><td>28</td><td>29</td><td>30</td><td class="off">1</td></tr>
    <tr class="wk"><td class="off">2</td><td class="off">3</td><td class="off">4</td><td class="off">5</td><td class="off">6</td><td class="off">7</td><td class="off">8</td></tr>
  </table>

  <footer class="abs footer"></footer>
  <div class="abs footer-links">Home | About Us | Schools | Events | Students | Gallery | Lectures | Contact Us</div>
  <div class="abs copyright">© 2015 Company Name &nbsp;All right reserved &nbsp;Term of Use</div>
  <div class="abs social"><i></i><i></i><i></i></div>

</div>
</body>
</html>
```